Boutique Technology Consultancy specialising is Electronic and physical security

We need to redo our existing outdated website. For your reference the link www.pelu.com.au

```html
<!DOCTYPE html>
<html lang="en">
<head>
<meta charset="utf-8">
<title>Pelu Services</title>
<link href="https://fonts.googleapis.com/css2?family=Montserrat:wght@400;500;600;700&display=swap" rel="stylesheet">
<style>
:root{
  --red:#c62828;
  --red-dark:#8e1f22;
  --ink:#111;
  --text:#555;
  --pale:#fdf0f0;
  --grey:#ececec;
  --white:#fff;
}
*{box-sizing:border-box;margin:0;padding:0}
html,body{width:1200px;height:4717px;overflow:hidden}
body{position:relative;background:var(--white);font-family:'Montserrat',sans-serif;color:var(--ink)}
.abs{position:absolute}
.center{text-align:center}
.section-title{position:absolute;left:0;width:1200px;text-align:center;font-size:40px;font-weight:500;letter-spacing:1px;color:var(--ink)}
.lead{position:absolute;left:170px;width:860px;text-align:center;font-size:16px;line-height:26px;color:var(--text)}

/* header */
.site-header{left:0;top:0;width:1200px;height:82px;background:var(--pale)}
.brand{display:flex;align-items:center;gap:10px;font-weight:600;color:var(--ink)}
.brand-mark{width:30px;height:30px;background:var(--red)}
.brand-name{font-size:42px;line-height:1;letter-spacing:1px}
.site-header .brand{position:absolute;left:114px;top:18px}
.nav{position:absolute;left:546px;top:33px;display:flex;gap:27px;font-size:13px;font-weight:600}

/* hero */
.hero{left:0;top:82px;width:1200px;height:580px;background:linear-gradient(180deg,#1b2350 0%,#3a3560 30%,#5c3a5e 55%,#1d1f3a 100%)}
.hero-title{left:0;width:1200px;text-align:center;color:var(--white)}
.btn-red{background:var(--red);color:var(--white);font-weight:600;font-size:16px;display:flex;align-items:center;justify-content:center}

/* cards */
.card{position:absolute;background:var(--white);box-shadow:0 2px 10px rgba(0,0,0,.18);overflow:hidden}
.service-card{top:876px;width:298px;height:392px}
.service-img{position:absolute;left:6px;top:6px;width:286px;height:216px}
.service-title{position:absolute;left:0;width:100%;top:236px;text-align:center;font-size:22px;font-weight:500;line-height:28px}
.service-list{position:absolute;left:0;width:100%;list-style:none;text-align:center;font-size:14px;color:var(--text);line-height:26px}
.service-list li::before{content:"";display:inline-block;width:10px;height:10px;border:3px solid var(--red);border-radius:50%;margin-right:4px;vertical-align:-1px}
.corner{position:absolute;right:0;bottom:0;width:92px;height:78px}
.slider-arrow{position:absolute;width:32px;height:32px;border:2px solid #6a1b3a;border-radius:50%}

/* about */
.about-text{left:601px;top:1440px;width:400px;color:var(--white)}
.about-text h2{font-size:40px;font-weight:500;letter-spacing:1px;margin-bottom:16px}
.about-text p{font-size:13.5px;line-height:26px}
.about-text b{font-weight:700}
.btn-dark{background:#000;color:var(--white);font-weight:600;font-size:14px;display:flex;align-items:center;justify-content:center}

/* team */
.team-card{top:2046px;width:298px;height:418px;text-align:center}
.avatar{position:absolute;left:50px;top:28px;width:198px;height:198px;border-radius:50%}
.team-name{position:absolute;top:246px;width:100%;font-size:20px;font-weight:600}
.team-role{position:absolute;top:278px;width:100%;font-size:13px;font-weight:600}
.team-bio{position:absolute;top:300px;left:26px;width:246px;font-size:13px;line-height:26px;color:var(--text)}

/* experience */
.tile{position:absolute;top:2763px;height:364px;border-bottom:5px solid var(--red)}
.tile-label{position:absolute;left:22px;bottom:40px;color:var(--white);font-size:16px;font-weight:600;line-height:25px}
.tile-feature{top:2724px;height:445px;border:5px solid var(--red);border-radius:4px}

/* contact */
.field{position:absolute;background:var(--white);font-size:12px;color:#777;padding:18px 14px}

/* locations */
.tab{position:absolute;top:3904px;height:88px;display:flex;align-items:center;justify-content:center;font-size:21px;font-weight:600;background:var(--grey)}
.tab.active{background:var(--red);color:var(--white)}
.loc-row{position:absolute;left:112px;display:flex;align-items:flex-start;gap:12px;font-size:16px;font-weight:500;line-height:28px}
.loc-icon{width:30px;height:30px;border-radius:50%;background:var(--red);flex:none}

/* footer */
.footer-col{position:absolute;top:4500px;color:var(--white)}
.footer-col h4{font-size:20px;font-weight:600;margin-bottom:16px}
.footer-col p{font-size:13px;line-height:27px;padding-left:18px;position:relative}
</style>
</head>
<body>

<header class="abs site-header">
  <div class="brand"><span class="brand-mark"></span><span class="brand-name">PELU</span></div>
  <nav class="nav"><span>WELCOME</span><span>EXPERIENCE</span><span>SERVICES</span><span>TEAM</span><span>ABOUT</span><span>CONTACT</span></nav>
</header>

<section class="abs hero" role="img" aria-label="Night city skyline with glowing data light trails"></section>
<svg class="abs" style="left:0;top:600px" width="1200" height="70" viewBox="0 0 1200 70">
  <polygon points="0,12 600,60 1200,12 1200,70 0,70" fill="#fff"/>
  <polygon points="0,8 600,50 1200,0 1200,12 600,60 0,12" fill="#c62828"/>
</svg>
<div class="abs hero-title" style="top:244px;font-size:31px;font-weight:600">WELCOME TO</div>
<div class="abs hero-title" style="top:280px;font-size:58px;font-weight:600">PELU SERVICES</div>
<div class="abs hero-title" style="top:362px;font-size:17px;font-weight:500;line-height:27px">YOUR TECHNOLOGY PROJECTS<br>MADE EASY.</div>
<div class="abs btn-red" style="left:524px;top:434px;width:147px;height:41px">Get Started</div>

<h2 class="section-title" style="top:738px">OUR SERVICES</h2>
<p class="lead" style="top:795px">Pelu Services provides independent professional services for projects as well as operations and maintenance. We offer end to end services including:</p>

<div class="slider-arrow" style="left:34px;top:1076px"></div>
<div class="slider-arrow" style="left:1130px;top:1076px"></div>

<article class="card service-card" style="left:112px">
  <div class="service-img" role="img" aria-label="Team reviewing server racks in a data centre" style="background:linear-gradient(135deg,#2d3b3a,#8a9ca0)"></div>
  <h3 class="service-title">Strategy</h3>
  <ul class="service-list" style="top:280px"><li>Technology roadmaps</li><li>Master standards</li><li>Asset management plans</li></ul>
  <svg class="corner" viewBox="0 0 92 78"><polygon points="92,0 92,78 0,78" fill="#c62828"/><polyline points="64,46 72,54 64,62" fill="none" stroke="#fff" stroke-width="3"/></svg>
</article>
<article class="card service-card" style="left:449px">
  <div class="service-img" role="img" aria-label="Sketched light bulb with project ideas" style="background:linear-gradient(135deg,#e9ecef,#b9c0c6)"></div>
  <h3 class="service-title">Projects</h3>
  <ul class="service-list" style="top:280px"><li>Audit</li><li>Design</li><li>Procurement</li></ul>
  <svg class="corner" viewBox="0 0 92 78"><polygon points="92,0 92,78 0,78" fill="#c62828"/><polyline points="64,46 72,54 64,62" fill="none" stroke="#fff" stroke-width="3"/></svg>
</article>
<article class="card service-card" style="left:786px">
  <div class="service-img" role="img" aria-label="Maintenance and repair icons on blue hexagons" style="background:linear-gradient(135deg,#1f5d8f,#5fa6d6)"></div>
  <h3 class="service-title">Operations and<br>maintenance</h3>
  <ul class="service-list" style="top:308px"><li>Audit</li><li>Design</li></ul>
  <svg class="corner" viewBox="0 0 92 78"><polygon points="92,0 92,78 0,78" fill="#c62828"/><polyline points="64,46 72,54 64,62" fill="none" stroke="#fff" stroke-width="3"/></svg>
</article>

<svg class="abs" style="left:0;top:1350px" width="1200" height="548" viewBox="0 0 1200 548">
  <defs><linearGradient id="aboutBg" x1="0" y1="0" x2="1" y2="0"><stop offset="0" stop-color="#c62828"/><stop offset="1" stop-color="#7a2226"/></linearGradient></defs>
  <polygon points="0,45 250,0 1200,40 1200,548 0,548" fill="url(#aboutBg)"/>
  <polyline points="404,108 556,108 556,218" fill="none" stroke="#fff" stroke-width="2"/>
  <polyline points="124,340 124,456 276,456" fill="none" stroke="#fff" stroke-width="2"/>
</svg>
<div class="abs" role="img" aria-label="Two colleagues reviewing documents in an office" style="left:152px;top:1477px;width:379px;height:293px;background:linear-gradient(135deg,#cfcac4,#6f6a66)"></div>
<div class="abs about-text">
  <h2>ABOUT US</h2>
  <p>Pelu Services was established in 2016 by Tom Harlan to provide technology consulting services to corporate and government clients with a focus on:<br>
  <b>Property/facilities management</b><br><b>Asset management</b><br><b>Development and Construction</b><br>
  In 2022, Pelu Services merged Vantra Group into its operations, bringing increased capacity and capability to the NSW office.</p>
</div>
<div class="abs btn-dark" style="left:601px;top:1760px;width:134px;height:42px">Read More</div>

<h2 class="section-title" style="top:1964px">OUR TEAM</h2>
<div class="slider-arrow" style="left:30px;top:2257px"></div>
<div class="slider-arrow" style="left:1130px;top:2257px"></div>
<article class="card team-card" style="left:110px">
  <div class="avatar" role="img" aria-label="Portrait of Tom Harlan" style="background:radial-gradient(circle,#c9a98e,#6e5a4a)"></div>
  <div class="team-name">Tom Harlan</div><div class="team-role">Principal Consultant</div>
  <p class="team-bio">Tom founded Pelu in 2016 and continues to lead the organisation nationally.</p>
</article>
<article class="card team-card" style="left:450px">
  <div class="avatar" role="img" aria-label="Portrait of Grant Ellis" style="background:radial-gradient(circle,#d8b9a4,#8d7466)"></div>
  <div class="team-name">Grant Ellis</div><div class="team-role">Principal Consultant</div>
  <p class="team-bio">Grant founded Vantra Group in 2016 and joined Pelu as a Director in 2022, taking over leadership of the NSW office.</p>
</article>
<article class="card team-card" style="left:789px">
  <div class="avatar" role="img" aria-label="Portrait of Mark Doyle" style="background:radial-gradient(circle,#c79f84,#5b4a40)"></div>
  <div class="team-name">Mark Doyle</div><div class="team-role">Senior Consultant</div>
  <p class="team-bio">Mark established Pelu's Queensland office in 2019 and leads all of Pelu's engagements in the northern states</p>
</article>

<h2 class="section-title" style="top:2558px">EXPERIENCE</h2>
<p class="lead" style="top:2627px">Pelu has a diverse range of project experience across a range of industries within both the public and private sectors. The following is a small sample of some of the clients and sites we have worked with.</p>

<div class="tile" role="img" aria-label="Glass dome shopping centre interior" style="left:108px;width:220px;background:linear-gradient(160deg,#8e8f93,#3c3f48)"><div class="tile-label">Central Arcade</div></div>
<div class="tile" role="img" aria-label="Aerial view of hospital buildings" style="left:623px;width:220px;background:linear-gradient(160deg,#9aa48f,#4e5650)"><div class="tile-label">City Women's<br>Hospital</div></div>
<div class="tile" role="img" aria-label="Tall blue glass office tower" style="left:852px;width:238px;background:linear-gradient(160deg,#a7c4e0,#2f4f7a)"><div class="tile-label">Tower One</div></div>
<div class="tile tile-feature" role="img" aria-label="Steel suspension bridge tower" style="left:328px;width:295px;background:linear-gradient(170deg,#8fb0c4,#3b4750)">
  <div class="tile-label" style="left:20px;bottom:44px;font-size:14px;font-weight:500;line-height:28px"><span style="font-size:17px;font-weight:600">Ridgeway</span><br>Virtual servers, network and<br>CCTV upgrade design and<br>project management for this</div>
</div>

<svg class="abs" style="left:0;top:3254px" width="1200" height="474" viewBox="0 0 1200 474">
  <defs><linearGradient id="contactBg" x1="0" y1="0" x2="1" y2="1"><stop offset="0" stop-color="#7a2226"/><stop offset="1" stop-color="#d32f2f"/></linearGradient></defs>
  <polygon points="0,0 1200,0 1200,430 950,474 0,432" fill="url(#contactBg)"/>
</svg>
<h2 class="section-title" style="top:3340px;color:#fff">CONTACT US</h2>
<div class="field" style="left:158px;top:3409px;width:285px;height:52px">Your Name</div>
<div class="field" style="left:456px;top:3409px;width:286px;height:52px">Email Address</div>
<div class="field" style="left:757px;top:3409px;width:285px;height:52px">Subject</div>
<div class="field" style="left:158px;top:3472px;width:884px;height:91px;padding-top:14px">Your Message</div>
<div class="abs btn-dark" style="left:511px;top:3591px;width:176px;height:42px">Submit</div>

<h2 class="section-title" style="top:3816px">OUR LOCATIONS</h2>
<div class="tab active" style="left:110px;width:324px">MELBOURNE OFFICE</div>
<div class="tab" style="left:434px;width:325px;border-right:2px solid #bbb">QUEENSLAND OFFICE</div>
<div class="tab" style="left:759px;width:329px">SYDNEY OFFICE</div>

<div class="loc-row" style="top:4056px"><span class="loc-icon"></span><span>Tom Harlan</span></div>
<div class="loc-row" style="top:4104px"><span class="loc-icon"></span><span>0400 123 456</span></div>
<div class="loc-row" style="top:4152px"><span class="loc-icon"></span><span>Level 2, 88 Harbour Rd,<br>Melbourne VIC 3000</span></div>
<p class="abs" style="left:112px;top:4228px;width:420px;font-size:16px;font-weight:500;line-height:28px">Victorian Private Security Business Registration Number: 000-123-45X</p>
<div class="abs" role="img" aria-label="Street map of the Melbourne office location" style="left:592px;top:4040px;width:487px;height:274px;border:5px solid var(--red);border-radius:8px;background:linear-gradient(135deg,#eef1f4,#d5dbe2)"></div>

<svg class="abs" style="left:0;top:4420px" width="1200" height="297" viewBox="0 0 1200 297">
  <polygon points="0,10 900,0 1200,18 1200,297 0,297" fill="#000"/>
  <line x1="110" y1="242" x2="1088" y2="242" stroke="#666" stroke-width="1"/>
</svg>
<div class="abs brand" style="left:114px;top:4500px;color:#fff"><span class="brand-mark"></span><span class="brand-name">PELU</span></div>
<div class="footer-col" style="left:388px"><h4>Sydney office</h4><p>0400 234 567</p><p>12 Wattle Lane,<br>Sydney NSW 2000</p></div>
<div class="footer-col" style="left:619px"><h4>Melbourne Office</h4><p>0400 123 456</p><p>Level 2, 88 Harbour Rd,<br>Melbourne VIC 3000</p></div>
<div class="footer-col" style="left:868px"><h4>Queensland Office</h4><p>0400 345 678</p><p>45 Reed Street,<br>Brisbane QLD 4000</p></div>
<p class="abs" style="left:0;top:4682px;width:1200px;text-align:center;color:#fff;font-size:13px">Copyright © Pelu Services | All Rights Reserved</p>

</body>
</html>
```